Q-Rolls Business Card

We are a modern retail clothing store. Established in 1994. I need a presentable card that will amaze vendors when given to them.

Front: Logo in middle
Info Side:

Name: Tomas Velder
Cell: 630-812-4463
Work: 630-917-3384 EXT. 417
Email: Tomas@q-rolls-example.com
Website: www.Q-rolls-example.com

Industry/Entity Type

Business

```html
<!DOCTYPE html>
<html lang="en">
<head>
<meta charset="utf-8">
<title>Q-Rolls Business Card</title>
<link href="https://fonts.googleapis.com/css2?family=Open+Sans:wght@400;600;700&display=swap" rel="stylesheet">
<style>
  :root {
    --backdrop: #e7e5e2;
    --card-black: #1b1b1b;
    --card-black-sheen: #2c2c2c;
    --card-white: #ffffff;
    --swoosh-light: #d4d4d4;
    --swoosh-mid: #a9a9a9;
    --ink: #1a1a1a;
    --ink-soft: #3a3a3a;
  }
  * { margin: 0; padding: 0; box-sizing: border-box; }
  html, body { width: 1200px; height: 900px; overflow: hidden; }
  body {
    background: var(--backdrop);
    font-family: "Open Sans", Arial, sans-serif;
    position: relative;
  }
  .card {
    position: absolute;
    left: 280px;
    width: 640px;
    height: 366px;
    border-radius: 4px;
    overflow: hidden;
    box-shadow: 0 10px 26px rgba(0,0,0,0.22);
  }
  .card-front { top: 62px; background: linear-gradient(90deg, var(--card-black) 0%, var(--card-black-sheen) 50%, var(--card-black) 100%); }
  .card-info { top: 472px; background: var(--card-black); }

  .brand-name {
    position: absolute;
    font-family: "Open Sans", Arial, sans-serif;
    font-weight: 700;
    letter-spacing: 2px;
    text-transform: uppercase;
    white-space: nowrap;
  }
  .card-front .brand-name {
    color: var(--card-white);
    font-size: 76px;
    left: 0; right: 0; top: 128px;
    text-align: center;
  }
  .card-info .brand-name {
    color: var(--ink);
    font-size: 46px;
    left: 270px; top: 40px;
  }
  .card-shape { position: absolute; inset: 0; }

  .contact {
    position: absolute;
    left: 52px; top: 104px;
    color: var(--ink-soft);
    font-size: 15px;
    line-height: 20px;
  }
  .contact-name { font-weight: 700; color: var(--ink); font-size: 16px; padding-left: 22px; }
  .contact-role, .contact-address { padding-left: 22px; }
  .contact-list { list-style: none; margin-top: 8px; }
  .contact-list li { display: flex; align-items: center; gap: 8px; height: 26px; font-size: 16px; white-space: nowrap; }
  .contact-icon { width: 14px; height: 14px; flex: none; }
</style>
</head>
<body>

<section class="card card-front" aria-label="Card front">
  <div class="brand-name">Q-Rolls</div>
</section>

<section class="card card-info" aria-label="Card info side">
  <svg class="card-shape" width="640" height="366" viewBox="0 0 640 366" aria-hidden="true">
    <ellipse cx="332" cy="168" rx="372" ry="206" transform="rotate(-6 332 168)" fill="var(--swoosh-light)"/>
    <ellipse cx="326" cy="176" rx="366" ry="198" transform="rotate(-6 326 176)" fill="var(--swoosh-mid)"/>
    <ellipse cx="320" cy="180" rx="360" ry="194" transform="rotate(-6 320 180)" fill="var(--card-white)"/>
  </svg>

  <div class="brand-name">Q-Rolls</div>

  <div class="contact">
    <p class="contact-name">Tomas Velder</p>
    <p class="contact-role">President</p>
    <p class="contact-address">418 Larchmere Road<br>Suite 9 Ridgeview, IL 60177</p>
    <ul class="contact-list">
      <li>
        <svg class="contact-icon" viewBox="0 0 14 14" aria-hidden="true"><path d="M3 1l2.5 3-1.5 1.5c.8 1.8 2.2 3.2 4 4L9.5 8 13 10.5 11.5 13C6 12.5 1.5 8 1 2.5z" fill="var(--ink-soft)"/></svg>
        630-917-3384 EXT. 417
      </li>
      <li>
        <svg class="contact-icon" viewBox="0 0 14 14" aria-hidden="true"><rect x="3.5" y="1" width="7" height="12" rx="1.3" fill="none" stroke="var(--ink-soft)" stroke-width="1.6"/><circle cx="7" cy="10.8" r="0.9" fill="var(--ink-soft)"/></svg>
        630-812-4463
      </li>
      <li>
        <svg class="contact-icon" viewBox="0 0 14 14" aria-hidden="true"><circle cx="7" cy="7" r="5.8" fill="none" stroke="var(--ink-soft)" stroke-width="1.3"/><ellipse cx="7" cy="7" rx="2.5" ry="5.8" fill="none" stroke="var(--ink-soft)" stroke-width="1.1"/><path d="M1.2 7h11.6" stroke="var(--ink-soft)" stroke-width="1.1"/></svg>
        www.Q-rolls-example.com
      </li>
      <li>
        <svg class="contact-icon" viewBox="0 0 14 14" aria-hidden="true"><text x="7" y="11.5" text-anchor="middle" font-family="Open Sans, Arial, sans-serif" font-size="14" font-weight="700" fill="var(--ink-soft)">@</text></svg>
        Tomas@q-rolls-example.com
      </li>
    </ul>
  </div>
</section>

</body>
</html>
```